Real Estate Company Looking for Business Card Designs for 3 Executives

Hello!
Thanks so much for considering our project! We are a real estate investment company located in Edmonton, Alberta called Marlbeck Group of Companies. We invest/develop both commercial and residential real estate and are looking to create 3 DOUBLE-SIDED business cards for 3 top executives in the company! (for some reason it won't let us select the double-sided option, but yes, the cards are double sided and would be happy to tip extra)

We have certain guidelines that we want our business cards to for sure follow - the back of the Business card has to be the Black Background Version of the Logo which has already been designed and linked as a file (first file). We want the entire back of the card to simply just be the black background logo. In terms of the front of the card, would like to see a smaller version of the white background logo (linked as the second file) in the top left hand corner - of course, feel free to get creative and we can make revisions together along the way! and Then after that, just text. We want the card to be sharp, clean, easy on the eyes and highly professional looking. We would like the card to include the Full name of the Company (Marlbeck Group of Companies), Name of the Person, Title, Phone, Email. If possible please provide the front part of the card for 3 people:

1) Marlbeck Group of Companies, Lena Okafor, Chief Financial Officer, 780-555-0162, lenaokafor@marlbeckgroup.example

2) Marlbeck Group of Companies, Tobias Okafor, Chief Executive Officer, 780-555-0148, tobiasokafor@marlbeckgroup.example

3) Marlbeck Group of Companies, Rui Dalton, Chief Operations Officer, 587-555-0193, ruidalton@marlbeckgroup.example

Thank you so much for considering our project & we look forward to seeing your designs!

```html
<!DOCTYPE html>
<html lang="en">
<head>
<meta charset="utf-8">
<title>Marlbeck Group of Companies – Business Card</title>
<link rel="stylesheet" href="https://fonts.googleapis.com/css2?family=Jost:wght@400;500;600&family=Oswald:wght@300;400&display=swap">
<style>
  :root {
    --stage: #a9a9a9;
    --card-black: #0a0708;
    --pattern-tone: #2a2627;
    --card-white: #ffffff;
    --ink: #111111;
    --ink-grey: #8e8e8e;
    --watermark: #f1f1f1;
  }
  * { margin: 0; padding: 0; box-sizing: border-box; }
  html, body { width: 1200px; height: 1000px; overflow: hidden; }
  body {
    background: var(--stage);
    position: relative;
    font-family: "Jost", "Helvetica Neue", Arial, sans-serif;
  }
  .card {
    position: absolute;
    left: 294px;
    width: 613px;
    height: 351px;
    border-radius: 18px;
    overflow: hidden;
  }
  /* Back side */
  .card-back { top: 82px; background: var(--card-black); }
  .back-pattern {
    position: absolute; inset: 0;
    background: linear-gradient(135deg, var(--pattern-tone) 0%, #1a1617 50%, var(--pattern-tone) 100%);
    opacity: 0.75;
  }
  .back-wordmark {
    position: absolute;
    right: 56px;
    top: 258px;
    padding: 6px 10px;
    background: var(--card-black);
    color: #ffffff;
    font-weight: 500;
    font-size: 15px;
    letter-spacing: 3px;
  }
  /* Front side */
  .card-front { top: 545px; background: var(--card-white); }
  .front-wordmark {
    position: absolute;
    left: 39px; top: 44px;
    color: var(--ink);
    font-weight: 500;
    font-size: 17px;
    letter-spacing: 3px;
  }
  .front-watermark {
    position: absolute;
    left: 290px; top: 150px;
    color: var(--watermark);
    font-weight: 500;
    font-size: 78px;
    letter-spacing: 8px;
    white-space: nowrap;
  }
  .company {
    position: absolute;
    right: 63px; top: 46px;
    text-align: left;
  }
  .company-name {
    font-weight: 600;
    font-size: 20px;
    letter-spacing: 3.4px;
    color: var(--ink);
    line-height: 24px;
  }
  .company-sub {
    font-family: "Oswald", "Arial Narrow", sans-serif;
    font-weight: 300;
    font-size: 15px;
    letter-spacing: 2.6px;
    color: var(--ink-grey);
    line-height: 20px;
  }
  .person { position: absolute; left: 37px; top: 170px; }
  .person-name {
    font-weight: 500;
    font-size: 26px;
    color: var(--ink);
    line-height: 34px;
  }
  .person-title {
    font-family: "Oswald", "Arial Narrow", sans-serif;
    font-weight: 300;
    font-size: 13px;
    letter-spacing: 2.6px;
    color: var(--ink-grey);
    margin-top: 4px;
  }
  .contact {
    position: absolute; left: 37px; top: 281px;
    font-size: 15.5px;
    color: var(--ink);
    line-height: 22px;
  }
</style>
</head>
<body>
  <div class="card card-back">
    <div class="back-pattern" role="img" aria-label="Repeating pattern of the company monogram in dark grey on black"></div>
    <div class="back-wordmark">MARLBECK</div>
  </div>

  <div class="card card-front">
    <div class="front-watermark" aria-hidden="true">MARLBECK</div>
    <div class="front-wordmark">MARLBECK</div>
    <div class="company">
      <div class="company-name">MARLBECK</div>
      <div class="company-sub">GROUP OF COMPANIES</div>
    </div>
    <div class="person">
      <div class="person-name">Lena Okafor</div>
      <div class="person-title">CHIEF FINANCIAL OFFICER</div>
    </div>
    <div class="contact">
      <div class="contact-phone">780-555-0162</div>
      <div class="contact-email">lenaokafor@marlbeckgroup.example</div>
    </div>
  </div>
</body>
</html>
```